Website for new crypto research organization

See brief (attached). This is a pretty basic website with only a handful of pages + ability to collect email addresses.

```html
<!DOCTYPE html>
<html lang="en">
<head>
<meta charset="utf-8">
<title>Cyanreef Digital — Website Design</title>
<link rel="stylesheet" href="https://fonts.googleapis.com/css2?family=Space+Grotesk:wght@400;500;600&family=Inter:wght@400;500&display=swap">
<style>
:root{
  --teal:#03a9a2;
  --light:#eeeeee;
  --panel:#ebebeb;
  --ink:#1e1e1e;
  --muted:#555555;
  --line:#d9d9d9;
  --white:#ffffff;
  --head:"Space Grotesk", sans-serif;
  --body:"Inter", Arial, sans-serif;
}
*{margin:0;padding:0;box-sizing:border-box}
html,body{width:1200px;height:3458px;overflow:hidden;background:var(--white)}
body{position:relative;font-family:var(--body);color:var(--ink)}
.abs{position:absolute}

/* brand sheet */
.brand-sheet{position:absolute;left:0;top:0;width:1200px;height:586px;background:var(--white)}
.sheet-logo{left:295px;top:108px;font:600 26px/1.1 var(--head);color:var(--teal);width:150px}
.sheet-divider{width:1px;height:84px;background:#bdbdbd;top:92px}
.sheet-label{font:400 21px var(--head);color:var(--ink)}
.sheet-font{font:400 18px/28px var(--head);color:#8a8a8a}
.swatch{width:38px;height:38px;border-radius:50%;top:121px}
.swatch-hex{top:166px;font:400 9px monospace;color:#555;width:50px;text-align:center}

/* site */
.site{position:absolute;left:0;top:586px;width:1200px;height:2872px;background:var(--light)}
section,header,footer{position:absolute;left:0;width:1200px}

.site-header{top:0;height:99px;background:#f2f2f2;border-bottom:1px solid var(--line)}
.wordmark{font:600 20px/1.1 var(--head);color:var(--teal)}
.site-header .wordmark{left:161px;top:28px;width:140px}
.nav a{position:absolute;top:42px;font:400 12px var(--body);color:#333;text-decoration:none}
.nav a.active{color:var(--teal);border-bottom:1px solid var(--teal);padding-bottom:4px}

.hero{top:99px;height:669px;background:#ececec}
.hero-visual{position:absolute;left:0;top:0;width:1200px;height:669px;
  background:linear-gradient(90deg,#f1f1f1 0%,#e6e6e6 42%,#c9c9c9 58%,#8f9a9a 68%,#14393c 76%,#0d2c2f 100%)}
.hero-title{left:161px;top:252px;font:500 39px/53px var(--head);color:var(--ink);letter-spacing:.5px}
.hero-title .mark{background:var(--teal);color:var(--white);padding:0 5px}
.hero-title .dot{color:var(--teal)}

.about{top:768px;height:742px;border-top:1px solid var(--line)}
.h2{font:500 28px var(--head);color:var(--ink)}
.h3{font:500 21px var(--head);color:var(--ink)}
.copy{font:400 11px/22px var(--body);color:var(--muted);width:430px}
.link-arrow{font:400 13px var(--body);color:var(--teal);display:flex;align-items:center;gap:12px}
.globe{left:722px;top:212px;width:350px;height:350px;border-radius:50%;
  background:radial-gradient(circle,#f3f3f3 0%,#e7e7e7 60%,#dedede 100%)}
.globe-name{left:722px;top:355px;width:350px;text-align:center;font:600 44px/1.1 var(--head);color:var(--teal)}

.research-head{top:1510px;height:229px;border-top:1px solid var(--line)}
.btn{background:var(--teal);color:var(--white);font:500 10px var(--body);letter-spacing:.5px;display:flex;align-items:center;justify-content:center;text-transform:uppercase}

.cards{top:1739px;height:526px;border-top:1px solid var(--line);border-bottom:1px solid var(--line)}
.card{position:absolute;top:0;width:400px;height:526px}
.card.featured{background:var(--teal)}
.card-date{left:59px;top:88px;font:400 11px var(--body);color:#555}
.tag{top:114px;height:27px;border:1px solid #bcbcbc;font:400 10px var(--body);color:#555;display:flex;align-items:center;justify-content:center}
.card-title{left:59px;top:172px;font:500 20px/26px var(--head);color:var(--ink);width:320px}
.card-more{left:59px;top:423px}
.featured .card-date,.featured .tag,.featured .card-title,.featured .card-more{color:var(--white)}
.featured .tag{border-color:rgba(255,255,255,.7)}

.subscribe{top:2265px;height:235px;border-bottom:1px solid var(--line)}
.sub-title{left:161px;top:86px;font:500 27px/34px var(--head)}
.email{left:633px;top:96px;width:277px;height:48px;border:1px solid #a8d9d6;background:var(--light);font:400 10px var(--body);color:#999;padding-left:20px;display:flex;align-items:center}

.site-footer{top:2500px;height:372px;background:#efefef}
.site-footer .wordmark{left:161px;top:96px;width:140px}
.disclaimer{left:161px;top:172px;width:360px;font:400 10px/23px var(--body);color:#555}
.foot-h{font:500 14px var(--head);color:var(--ink)}
.foot-rule{height:1px;width:38px;background:var(--teal);top:129px}
.foot-link{font:400 10px var(--body);color:#555;left:681px}
.social{width:29px;height:29px;background:var(--teal);top:155px}
</style>
</head>
<body>

<div class="brand-sheet">
  <div class="abs sheet-logo">Cyanreef Digital</div>
  <div class="abs sheet-divider" style="left:514px"></div>
  <div class="abs sheet-label" style="left:590px;top:90px">Fonts:</div>
  <div class="abs sheet-font" style="left:590px;top:131px">Px<br>Grotesk</div>
  <div class="abs sheet-divider" style="left:710px"></div>
  <div class="abs sheet-label" style="left:786px;top:88px">Colors:</div>
  <div class="abs swatch" style="left:786px;background:var(--teal)"></div>
  <div class="abs swatch" style="left:834px;background:var(--light)"></div>
  <div class="abs swatch" style="left:880px;background:var(--ink)"></div>
  <div class="abs swatch-hex" style="left:780px">#03a9a2</div>
  <div class="abs swatch-hex" style="left:828px">#eeeeee</div>
  <div class="abs swatch-hex" style="left:874px">#1e1e1e</div>
</div>

<main class="site">
  <header class="site-header">
    <div class="abs wordmark">Cyanreef Digital</div>
    <nav class="nav">
      <a class="active" href="#" style="left:597px">Home</a>
      <a href="#" style="left:664px">About</a>
      <a href="#" style="left:731px">Research</a>
      <a href="#" style="left:815px">Careers</a>
      <a href="#" style="left:890px">News</a>
      <a href="#" style="left:955px">Contact</a>
    </nav>
  </header>

  <section class="hero">
    <div class="hero-visual" role="img" aria-label="Photo of a hand pulling back a pale curtain to reveal a dark teal digital scene with a glowing coin emblem"></div>
    <h1 class="abs hero-title">Cyanreef <span class="mark">Digital</span><br>is a research-driven<br>digital asset<span class="dot">.</span></h1>
  </section>

  <section class="about">
    <h2 class="abs h2" style="left:161px;top:82px">About Us</h2>
    <p class="abs copy" style="left:161px;top:128px">Lorem ipsum dolor sit amet, consectetur adipiscing elit, sed do eiusmod tempor incididunt ut labore et dolore magna aliqua. Quis ipsum suspendisse ultrices gravida. Risus commodo viverra maecenas accumsan lacus vel.</p>
    <div class="abs link-arrow" style="left:161px;top:228px">Meet our team
      <svg width="18" height="10" viewBox="0 0 18 10"><path d="M0 5h16M12 1l4 4-4 4" fill="none" stroke="#03a9a2" stroke-width="1.2"/></svg></div>

    <h3 class="abs h3" style="left:161px;top:326px">Who we are</h3>
    <p class="abs copy" style="left:161px;top:367px;width:460px">A thematic, research-driven digital asset investment firm built for founders.</p>
    <h3 class="abs h3" style="left:161px;top:438px">Vision</h3>
    <p class="abs copy" style="left:161px;top:479px">Web3, blockchain technology, and digital assets will drive the largest wealth shift in the global economy since the advent of the internet</p>
    <h3 class="abs h3" style="left:161px;top:572px">Mission</h3>
    <p class="abs copy" style="left:161px;top:612px">We apply a principled digital asset investment strategy and partner with founders to enable their token-based decentralized networks to scale</p>

    <div class="abs globe" role="img" aria-label="Faint wireframe network globe illustration"></div>
    <div class="abs globe-name">Cyanreef Digital</div>
  </section>

  <section class="research-head">
    <h2 class="abs h2" style="left:161px;top:98px">Research</h2>
    <div class="abs btn" style="left:910px;top:91px;width:128px;height:48px">Discover more</div>
  </section>

  <section class="cards">
    <article class="card" style="left:0">
      <div class="abs card-date">07/02/2022</div>
      <div class="abs tag" style="left:59px;width:90px">RESEARCH</div>
      <div class="abs tag" style="left:155px;width:89px">CRYPTO</div>
      <div class="abs tag" style="left:250px;width:89px">BLOCKCHAIN</div>
      <h3 class="abs card-title">Lorem ipsum dolor sitot:<br>Consectetur adipiscinget</h3>
      <div class="abs link-arrow card-more">read more
        <svg width="18" height="10" viewBox="0 0 18 10"><path d="M0 5h16M12 1l4 4-4 4" fill="none" stroke="#03a9a2" stroke-width="1.2"/></svg></div>
    </article>
    <article class="card featured" style="left:399px">
      <div class="abs card-date">07/02/2022</div>
      <div class="abs tag" style="left:59px;width:90px">RESEARCH</div>
      <div class="abs tag" style="left:155px;width:89px">CRYPTO</div>
      <div class="abs tag" style="left:250px;width:89px">BLOCKCHAIN</div>
      <h3 class="abs card-title">Lorem ipsum dolor sitot:<br>Consectetur adipiscinget</h3>
      <div class="abs link-arrow card-more">read more
        <svg width="18" height="10" viewBox="0 0 18 10"><path d="M0 5h16M12 1l4 4-4 4" fill="none" stroke="#ffffff" stroke-width="1.2"/></svg></div>
    </article>
    <article class="card" style="left:799px">
      <div class="abs card-date">07/02/2022</div>
      <div class="abs tag" style="left:59px;width:90px">RESEARCH</div>
      <div class="abs tag" style="left:155px;width:89px">CRYPTO</div>
      <div class="abs tag" style="left:250px;width:89px">BLOCKCHAIN</div>
      <h3 class="abs card-title">Lorem ipsum dolor sitot:<br>Consectetur adipiscinget</h3>
      <div class="abs link-arrow card-more">read more
        <svg width="18" height="10" viewBox="0 0 18 10"><path d="M0 5h16M12 1l4 4-4 4" fill="none" stroke="#03a9a2" stroke-width="1.2"/></svg></div>
    </article>
  </section>

  <section class="subscribe">
    <h2 class="abs sub-title">Subscribe To<br>Cyanreef Digital</h2>
    <div class="abs email">Type your email address here</div>
    <div class="abs btn" style="left:910px;top:96px;width:128px;height:48px">Subscribe</div>
  </section>

  <footer class="site-footer">
    <div class="abs wordmark">Cyanreef Digital</div>
    <p class="abs disclaimer">This site is not intended to provide any investment, financial, legal, regulatory, accounting, tax or similar advice, and nothing on this site should be construed as a recommendation by Cyanreef Digital, its affiliates, or any third party, to acquire or dispose of any investment, or to engage in any investment strategy or transaction.</p>

    <div class="abs foot-h" style="left:681px;top:88px">Quick Links</div>
    <div class="abs foot-rule" style="left:681px"></div>
    <div class="abs foot-link" style="top:155px">About</div>
    <div class="abs foot-link" style="top:184px">Research</div>
    <div class="abs foot-link" style="top:213px">Careers</div>
    <div class="abs foot-link" style="top:242px">Team</div>
    <div class="abs foot-link" style="top:271px">Contact</div>

    <div class="abs foot-h" style="left:933px;top:88px">Follow Us</div>
    <div class="abs foot-rule" style="left:933px"></div>
    <div class="abs social" style="left:933px" aria-label="Social link"></div>
    <div class="abs social" style="left:971px" aria-label="Social link"></div>
    <div class="abs social" style="left:1009px" aria-label="Social link"></div>
  </footer>
</main>

</body>
</html>
```